Up to the Challenge? Canadian based consulting company needs a two sided business card design

A Canadian based security risk management consulting company needs a two-sided business card design. What we do is provide advice and guidance related to emergency, security and business continuity management for small, medium and large companies to help ensure the protection of their people, assets, information, services, operations and reputation.

The final design should be simple, only one or two colours, eye catching, professional and one that makes people look at three or more times just because it looks so darn good.

I have include examples of business cards I like.

Target Market(s)

Small, medium and large companies.

Industry/Entity Type

Security

Contact Information for Business Card

Business Card Size: Standard size of 3.5" (89mm) x 2.0" (51mm) - (see full specifications and guides on PRINTA's website if required)
Card Stock: Looking to use PRINTA's Velda 32pt stock textured paper - seam colour either chili red or black
Business Name: The Harrowfield Group
Website: www.theharrowfieldgroup.example
Telephone: (555)214-0397
Name: Dana Forsythe
Position: Principle
e-mail: Dana.Forsythe@theharrowfieldgroup.example

Font styles to use
Serif

Colors
ec1f27
000000
9d9d9d
aaaaaa
606060

Requirements
Must have
• - "The Harrowfield Group" logo (see uploaded files). I have included grey scale and colour versions.
• - Business card details (as above)
Nice to have
• - One side black or grey scale.
• - Other side would likely be white.
• - Everyone likes the silver logo on the black background.
• - Small element of colour i.e. red but I'm leaning more to greyscale.
Should not have
• - A lot of colour. Keep it simple.

```html
<!DOCTYPE html>
<html lang="en">
<head>
<meta charset="utf-8">
<title>The Harrowfield Group – Business Card</title>
<link rel="stylesheet" href="https://fonts.googleapis.com/css2?family=Cinzel:wght@600&family=Arimo:wght@400;700&display=swap">
<style>
  :root {
    --backdrop: #5a4939;
    --paper: #ffffff;
    --panel-grey: #6a6a6c;
    --stripe-dark: #4a4a4c;
    --logo-grey: #606060;
    --card-black: #0e0e0e;
    --back-logo: #5c5c5c;
    --back-url: #454545;
    --light-text: #ffffff;
  }
  * { margin: 0; padding: 0; box-sizing: border-box; }
  html, body { width: 1200px; height: 987px; overflow: hidden; }
  body { background: var(--backdrop); position: relative; }

  .card {
    position: absolute;
    width: 615px;
    height: 352px;
    overflow: hidden;
    box-shadow: 0 2px 6px rgba(0,0,0,0.35);
  }
  .card--front { left: 293px; top: 130px; background: var(--paper); }
  .card--back { left: 292px; top: 505px; background: var(--card-black); }

  .front-shapes { position: absolute; inset: 0; }

  .brand {
    position: absolute;
    display: flex;
    flex-direction: column;
    align-items: center;
    font-family: "Cinzel", Georgia, serif;
    font-weight: 600;
    color: var(--logo-grey);
    text-align: center;
  }
  .brand__mark { border-radius: 50%; background: currentColor; }
  .brand__name { line-height: 1; white-space: nowrap; }
  .brand__sub { line-height: 1; letter-spacing: 0.08em; }

  .card--front .brand { left: 0; width: 280px; top: 104px; }
  .card--front .brand__mark { width: 76px; height: 76px; margin-bottom: 20px; }
  .card--front .brand__name { font-size: 23px; }
  .card--front .brand__sub { font-size: 17px; margin-top: 4px; }

  .card--back .brand { left: 0; width: 615px; top: 72px; color: var(--back-logo); }
  .card--back .brand__mark { width: 100px; height: 100px; margin-bottom: 22px; }
  .card--back .brand__name { font-size: 36px; }
  .card--back .brand__sub { font-size: 25px; margin-top: 6px; }

  .person {
    position: absolute;
    right: 17px;
    top: 40px;
    text-align: right;
    font-family: "Arimo", Arial, sans-serif;
    color: var(--light-text);
  }
  .person__name { font-size: 21px; font-weight: 700; line-height: 1.2; }
  .person__title { font-size: 16px; line-height: 1.3; margin-top: 2px; }

  .contact {
    position: absolute;
    right: 17px;
    top: 215px;
    list-style: none;
    text-align: right;
    font-family: "Arimo", Arial, sans-serif;
    font-size: 13px;
    color: var(--light-text);
  }
  .contact__item {
    height: 23.5px;
    display: flex;
    justify-content: flex-end;
    align-items: center;
    gap: 7px;
    white-space: nowrap;
  }
  .contact__item--email { font-size: 11.5px; letter-spacing: -0.2px; }
  .contact__icon { width: 16px; height: 16px; flex: none; }
  .contact__square { width: 15px; height: 15px; background: var(--light-text); flex: none; margin-right: 1px; }

  .back-url {
    position: absolute;
    left: 0;
    width: 615px;
    top: 297px;
    text-align: center;
    font-family: "Arimo", Arial, sans-serif;
    font-size: 13px;
    letter-spacing: 4px;
    color: var(--back-url);
  }
</style>
</head>
<body>
  <section class="card card--front" aria-label="Business card front">
    <svg class="front-shapes" width="615" height="352" viewBox="0 0 615 352" aria-hidden="true">
      <polygon points="290,0 615,0 615,352 290,352 378,176" fill="var(--panel-grey)"/>
      <polyline points="279,-2 384,176 281,354" fill="none" stroke="var(--stripe-dark)" stroke-width="4"/>
    </svg>

    <div class="brand">
      <span class="brand__mark"></span>
      <span class="brand__name">The Harrowfield</span>
      <span class="brand__sub">Group</span>
    </div>

    <div class="person">
      <p class="person__name">Dana Forsythe</p>
      <p class="person__title">Principle</p>
    </div>

    <ul class="contact">
      <li class="contact__item">
        <span>(555)214-0397</span>
        <svg class="contact__icon" viewBox="0 0 16 16" aria-hidden="true">
          <path d="M1 6 C1 2.5 15 2.5 15 6 L15 7.5 L11.5 7.5 L11.5 5.8 C10 5 6 5 4.5 5.8 L4.5 7.5 L1 7.5 Z" fill="#fff"/>
          <path d="M4 8.5 L12 8.5 L14 14 L2 14 Z" fill="#fff"/>
          <circle cx="8" cy="11" r="1.6" fill="var(--panel-grey)"/>
        </svg>
      </li>
      <li class="contact__item">
        <span>adanaforsythe</span>
        <span class="contact__square"></span>
      </li>
      <li class="contact__item contact__item--email"><span>Dana.Forsythe@theharrowfieldgroup.example</span></li>
      <li class="contact__item"><span>www.theharrowfieldgroup.example</span></li>
    </ul>
  </section>

  <section class="card card--back" aria-label="Business card back">
    <div class="brand">
      <span class="brand__mark"></span>
      <span class="brand__name">The Harrowfield</span>
      <span class="brand__sub">Group</span>
    </div>
    <p class="back-url">www.theharrowfieldgroup.example</p>
  </section>
</body>
</html>
```